Menu Design Project

We are looking for a re-design of our menu.

We are an italian restaurant.

More info here:

http://www.dinerscout.com/Restaurant_Review-g51273-d604518-Reviews-Velluto-Rockland_Maine.html

website: vellutorestaurant.com

Industry/Entity Type

Restaurant

Requirements
Must have
• Italian Design

Italian Colors

Easy to customize so we can add our own stuff quick

No need for heavy graphics or heavy colors

```html
<!DOCTYPE html>
<html lang="en">
<head>
<meta charset="utf-8">
<title>Velluto Menu</title>
<link href="https://fonts.googleapis.com/css2?family=Roboto+Condensed:wght@300;400&display=swap" rel="stylesheet">
<style>
:root{
  --paper:#c4b59c;
  --olive:#4f4e24;
  --ink:#37321c;
  --label:#d6cbb3;
  --flag-green:#129747;
  --flag-white:#ffffff;
  --flag-red:#d62a3a;
}
*{margin:0;padding:0;box-sizing:border-box}
html,body{width:1018px;height:1200px;overflow:hidden;background:var(--paper)}
body{font-family:"Roboto Condensed","Arial Narrow",sans-serif;color:var(--ink)}
.menu{position:relative;width:1018px;height:1200px}
.panel{position:absolute;top:0;width:509px;height:1200px;background:var(--paper)}
.panel--left{left:0}
.panel--right{left:509px}
.panel__band{position:absolute;left:0;top:0;width:52px;height:100%;background:var(--olive)}
.panel__rule{position:absolute;left:128px;top:0;width:1px;height:100%;background:var(--olive)}
.flag{position:absolute;left:128px;top:0;width:176px;height:50px;display:flex}
.flag span{flex:1}
.flag .green{background:var(--flag-green)}
.flag .white{background:var(--flag-white)}
.flag .red{background:var(--flag-red)}
.section-label{position:absolute;left:26px;transform-origin:0 0;transform:rotate(-90deg) translate(-100%,-50%);
  font-weight:300;font-size:22px;letter-spacing:6px;color:var(--label);white-space:nowrap;line-height:1}
.section-label--starters{top:85px;width:168px}
.section-label--pasta{top:840px;width:80px}
.item{position:absolute;left:0;width:509px}
.item__price{position:absolute;left:71px;top:0;font-size:15px;font-weight:300;letter-spacing:.2px}
.item__body{position:absolute;left:146px;top:0;width:350px}
.item__name{font-size:16px;font-weight:300;line-height:19px;transform:scaleX(.88);transform-origin:0 0;white-space:nowrap}
.item__desc{font-size:11.5px;font-weight:400;line-height:14.6px;transform:scaleX(.86);transform-origin:0 0;white-space:nowrap}
</style>
</head>
<body>
<main class="menu">
  <section class="panel panel--left">
    <div class="panel__band"></div>
    <div class="panel__rule"></div>
    <div class="flag"><span class="green"></span><span class="white"></span><span class="red"></span></div>
    <h2 class="section-label section-label--starters">APPRTIZERS</h2>
    <h2 class="section-label section-label--pasta">PASTA</h2>

    <div class="item" style="top:85px"><span class="item__price">$18.00</span><div class="item__body"><p class="item__name">Wood Fired Pizza</p><p class="item__desc">Garlic, Crp And 4 Cheeses, Finished With Arugula,<br>Tomatoes, Basil And Garlic Aïoli</p></div></div>
    <div class="item" style="top:152px"><span class="item__price">$11.00</span><div class="item__body"><p class="item__name">Tender Garden Spring Lettuces &amp; Herbs</p><p class="item__desc">With House Barrel-aged Red Wine Vinaigrette</p></div></div>
    <div class="item" style="top:205px"><span class="item__price">$18.00</span><div class="item__body"><p class="item__name">Cedar Valley Foie Gras Two Ways</p><p class="item__desc">Seared Atop Toasted Zucchini Bread With Almond Butter And<br>Black Pepper-strawberry Jam Au Torchon With A Local Strawberry And<br>Gooseberry Salad, Anise Basil</p></div></div>
    <div class="item" style="top:287px"><span class="item__price">$15.00</span><div class="item__body"><p class="item__name">Salad Of Red Lettuces<br>With Fig In Pig Drizzled With A Port Wine Syrup</p><p class="item__desc">Tender Baby Red Lettuces And Garden Greens Tossed<br>With Gorgonzola Dressing, Toasted Fruit And Nut Crostini</p></div></div>
    <div class="item" style="top:373px"><span class="item__price">$12.00</span><div class="item__body"><p class="item__name">Nora's Escarole Salad</p><p class="item__desc">Radicchio, Shaved Red Onion, Pecorino, Toasted Walnuts<br>And A Creamy Anchovy Dressing</p></div></div>
    <div class="item" style="top:440px"><span class="item__price">$16.00</span><div class="item__body"><p class="item__name">Chilled Octopus Terrine</p><p class="item__desc">Salad Of Shaved Chorizo, Frisee, Petite Celery<br>And Honeydrop Peppers ...white Bean Crostini</p></div></div>
    <div class="item" style="top:508px"><span class="item__price">$17.00</span><div class="item__body"><p class="item__name">Velluto Charcuterie</p><p class="item__desc">Pate, Fennel Coppa, Lonza, Juniper Lardo, Mortadella...radish,<br>Pickles And Toasted Baguette, Rustic Dijon Mustard</p></div></div>
    <div class="item" style="top:575px"><span class="item__price">$15.00</span><div class="item__body"><p class="item__name">Bread And Fish Soup</p><p class="item__desc">Bay Of Fundy Halibut, Leeks And Grilled Levain In<br>A Saffron Infused Tomato-fish Broth, Swirled With Rouille</p></div></div>
    <div class="item" style="top:642px"><span class="item__price">$14.00</span><div class="item__body"><p class="item__name">Farmer Salad</p><p class="item__desc">Frisée, Romaine And Radicchio Lettuces Tossed<br>With A Lemon-parmesan Vinaigrette Olive Oil Fried Croutons,<br>House-made Bacon And A Backyard Poached Egg</p></div></div>
    <div class="item" style="top:723px"><span class="item__price">$17.00</span><div class="item__body"><p class="item__name">Chilled Harbor Point Oysters On The Half Shell</p><p class="item__desc">Gazpacho Sauce, Cucumber Relish And Petite Celery Leaf</p></div></div>

    <div class="item" style="top:839px"><span class="item__price">$32.00</span><div class="item__body"><p class="item__name">Spaghetti And Clams</p><p class="item__desc">Steamed Seacove Littlenecks With Blistered Tomatoes And Rapini Pesto</p></div></div>
    <div class="item" style="top:891px"><span class="item__price">$29.00</span><div class="item__body"><p class="item__name">Spinach Pappardelle With A Spicy Bolognese</p><p class="item__desc">Locally Raised At Meadowbrook Farm Baby Spinach, Roasted<br>Tomatoes, Garden Chiles And Lots Of Basil</p></div></div>
    <div class="item" style="top:954px"><span class="item__price">$28.00</span><div class="item__body"><p class="item__name">Saffron Linguine With Smoked Swordfish</p><p class="item__desc">"Sicilian Style" Fried Eggplant, Capers, Basil, Mint And<br>Rapini In A Tomato Passato Sauce</p></div></div>
    <div class="item" style="top:1018px"><span class="item__price">$30.00</span><div class="item__body"><p class="item__name">Spinach Pappardelle With A Spicy Bolognese</p><p class="item__desc">Swiss Chard, Roasted Tomatoes And Housemade Silky Ricotta</p></div></div>
    <div class="item" style="top:1066px"><span class="item__price">$32.00</span><div class="item__body"><p class="item__name">Local Wild Mushrooms With Porcini Tagliatelle</p><p class="item__desc">Chanterelle, Lobster, Black Trumpet And Alba, Spinach And<br>Thyme In A Mushroom Broth, Finished With Reggiano</p></div></div>
  </section>

  <section class="panel panel--right">
    <div class="panel__band"></div>
    <div class="panel__rule"></div>
    <div class="flag"><span class="green"></span><span class="white"></span><span class="red"></span></div>
    <h2 class="section-label section-label--starters">APPRTIZERS</h2>
    <h2 class="section-label section-label--pasta">PASTA</h2>

    <div class="item" style="top:85px"><span class="item__price">$18.00</span><div class="item__body"><p class="item__name">Wood Fired Pizza</p><p class="item__desc">Garlic, Crp And 4 Cheeses, Finished With Arugula,<br>Tomatoes, Basil And Garlic Aïoli</p></div></div>
    <div class="item" style="top:152px"><span class="item__price">$11.00</span><div class="item__body"><p class="item__name">Tender Garden Spring Lettuces &amp; Herbs</p><p class="item__desc">With House Barrel-aged Red Wine Vinaigrette</p></div></div>
    <div class="item" style="top:205px"><span class="item__price">$18.00</span><div class="item__body"><p class="item__name">Cedar Valley Foie Gras Two Ways</p><p class="item__desc">Seared Atop Toasted Zucchini Bread With Almond Butter And<br>Black Pepper-strawberry Jam Au Torchon With A Local Strawberry And<br>Gooseberry Salad, Anise Basil</p></div></div>
    <div class="item" style="top:287px"><span class="item__price">$15.00</span><div class="item__body"><p class="item__name">Salad Of Red Lettuces<br>With Fig In Pig Drizzled With A Port Wine Syrup</p><p class="item__desc">Tender Baby Red Lettuces And Garden Greens Tossed<br>With Gorgonzola Dressing, Toasted Fruit And Nut Crostini</p></div></div>
    <div class="item" style="top:373px"><span class="item__price">$12.00</span><div class="item__body"><p class="item__name">Nora's Escarole Salad</p><p class="item__desc">Radicchio, Shaved Red Onion, Pecorino, Toasted Walnuts<br>And A Creamy Anchovy Dressing</p></div></div>
    <div class="item" style="top:440px"><span class="item__price">$16.00</span><div class="item__body"><p class="item__name">Chilled Octopus Terrine</p><p class="item__desc">Salad Of Shaved Chorizo, Frisee, Petite Celery<br>And Honeydrop Peppers ...white Bean Crostini</p></div></div>
    <div class="item" style="top:508px"><span class="item__price">$17.00</span><div class="item__body"><p class="item__name">Velluto Charcuterie</p><p class="item__desc">Pate, Fennel Coppa, Lonza, Juniper Lardo, Mortadella...radish,<br>Pickles And Toasted Baguette, Rustic Dijon Mustard</p></div></div>
    <div class="item" style="top:575px"><span class="item__price">$15.00</span><div class="item__body"><p class="item__name">Bread And Fish Soup</p><p class="item__desc">Bay Of Fundy Halibut, Leeks And Grilled Levain In<br>A Saffron Infused Tomato-fish Broth, Swirled With Rouille</p></div></div>
    <div class="item" style="top:642px"><span class="item__price">$14.00</span><div class="item__body"><p class="item__name">Farmer Salad</p><p class="item__desc">Frisée, Romaine And Radicchio Lettuces Tossed<br>With A Lemon-parmesan Vinaigrette Olive Oil Fried Croutons,<br>House-made Bacon And A Backyard Poached Egg</p></div></div>
    <div class="item" style="top:723px"><span class="item__price">$17.00</span><div class="item__body"><p class="item__name">Chilled Harbor Point Oysters On The Half Shell</p><p class="item__desc">Gazpacho Sauce, Cucumber Relish And Petite Celery Leaf</p></div></div>

    <div class="item" style="top:839px"><span class="item__price">$32.00</span><div class="item__body"><p class="item__name">Spaghetti And Clams</p><p class="item__desc">Steamed Seacove Littlenecks With Blistered Tomatoes And Rapini Pesto</p></div></div>
    <div class="item" style="top:891px"><span class="item__price">$29.00</span><div class="item__body"><p class="item__name">Spinach Pappardelle With A Spicy Bolognese</p><p class="item__desc">Locally Raised At Meadowbrook Farm Baby Spinach, Roasted<br>Tomatoes, Garden Chiles And Lots Of Basil</p></div></div>
    <div class="item" style="top:954px"><span class="item__price">$28.00</span><div class="item__body"><p class="item__name">Saffron Linguine With Smoked Swordfish</p><p class="item__desc">"Sicilian Style" Fried Eggplant, Capers, Basil, Mint And<br>Rapini In A Tomato Passato Sauce</p></div></div>
    <div class="item" style="top:1018px"><span class="item__price">$30.00</span><div class="item__body"><p class="item__name">Spinach Pappardelle With A Spicy Bolognese</p><p class="item__desc">Swiss Chard, Roasted Tomatoes And Housemade Silky Ricotta</p></div></div>
    <div class="item" style="top:1066px"><span class="item__price">$32.00</span><div class="item__body"><p class="item__name">Local Wild Mushrooms With Porcini Tagliatelle</p><p class="item__desc">Chanterelle, Lobster, Black Trumpet And Alba, Spinach And<br>Thyme In A Mushroom Broth, Finished With Reggiano</p></div></div>
  </section>
</main>
</body>
</html>
```